Kit com 6 Layouts de Post para Redes Sociais (Facebook, Instagram e etc) + Capa de Facebookpara RZ SEGUROS E CONSORCIOS
Postado por: gestao.rzseguros_2840395726   Estou Offline

```html
<!DOCTYPE html>
<html lang="pt-BR">
<head>
<meta charset="UTF-8">
<title>Post – Seu Texto Aqui</title>
<link href="https://fonts.googleapis.com/css2?family=Lexend:wght@400;500;600&display=swap" rel="stylesheet">
<style>
  :root {
    --deep-purple: #4a2a6c;
    --deep-purple-dark: #3d2159;
    --magenta: #c663cc;
    --magenta-soft: #d98fdc;
    --accent-pink: #d77ee0;
    --white: #ffffff;
  }
  html, body {
    margin: 0;
    padding: 0;
    width: 1200px;
    height: 1200px;
    overflow: hidden;
    background: var(--deep-purple);
  }
  .post {
    position: relative;
    width: 1200px;
    height: 1200px;
    overflow: hidden;
    font-family: "Lexend", sans-serif;
    color: var(--white);
  }
  .post__art {
    position: absolute;
    inset: 0;
    width: 1200px;
    height: 1200px;
  }
  .headline {
    position: absolute;
    left: 88px;
    top: 300px;
    margin: 0;
    font-size: 96px;
    font-weight: 600;
    line-height: 96px;
    letter-spacing: -2px;
  }
  .contact {
    position: absolute;
    left: 90px;
    top: 1040px;
  }
  .contact__label {
    position: absolute;
    left: 72px;
    top: 0;
    font-size: 17px;
    font-weight: 500;
    color: var(--accent-pink);
    white-space: nowrap;
  }
  .contact__phone {
    position: absolute;
    left: 0;
    top: 24px;
    display: flex;
    align-items: center;
    gap: 10px;
    white-space: nowrap;
  }
  .contact__icon {
    width: 34px;
    height: 34px;
    border-radius: 50%;
    background: var(--accent-pink);
    display: flex;
    align-items: center;
    justify-content: center;
  }
  .contact__number {
    font-size: 29px;
    font-weight: 600;
  }
  .contact__number small {
    font-size: 20px;
    font-weight: 500;
  }
  .contact__social {
    position: absolute;
    left: 46px;
    top: 72px;
    display: flex;
    align-items: center;
    gap: 8px;
    white-space: nowrap;
    font-size: 17px;
    font-weight: 400;
  }
  .contact__dot {
    width: 16px;
    height: 16px;
    border-radius: 50%;
    background: var(--accent-pink);
  }
  .brand-name {
    position: absolute;
    left: 858px;
    top: 1052px;
    font-size: 40px;
    font-weight: 500;
    white-space: nowrap;
  }
</style>
</head>
<body>
<main class="post">
  <svg class="post__art" viewBox="0 0 1200 1200" xmlns="http://www.w3.org/2000/svg">
    <defs>
      <linearGradient id="bgPhoto" x1="0" y1="0" x2="1" y2="1">
        <stop offset="0" stop-color="#b85cc0"/>
        <stop offset="0.5" stop-color="#d27ad6"/>
        <stop offset="1" stop-color="#c25fc8"/>
      </linearGradient>
      <linearGradient id="couplePhoto" x1="0" y1="0" x2="1" y2="1">
        <stop offset="0" stop-color="#a48a7e"/>
        <stop offset="0.45" stop-color="#e2b49a"/>
        <stop offset="1" stop-color="#4a3a3a"/>
      </linearGradient>
      <clipPath id="leftHalf"><rect x="0" y="0" width="748" height="1200"/></clipPath>
    </defs>

    <rect x="0" y="0" width="748" height="1200" fill="var(--deep-purple)"/>
    <rect x="748" y="0" width="452" height="1200" fill="url(#bgPhoto)" role="img" aria-label="Fotografia desfocada do casal em tons de magenta"/>

    <circle cx="775" cy="540" r="490" fill="var(--deep-purple-dark)" opacity="0.55" clip-path="url(#leftHalf)"/>
    <circle cx="775" cy="540" r="490" fill="#a450ab" opacity="0.35"/>

    <circle cx="775" cy="540" r="350" fill="url(#couplePhoto)" role="img" aria-label="Fotografia de um casal sorridente abraçado"/>
    <circle cx="775" cy="540" r="350" fill="#6a3d8c" opacity="0.82" clip-path="url(#leftHalf)"/>

    <path d="M 920 165 A 400 400 0 0 1 1180 470" fill="none" stroke="var(--white)" stroke-width="3"/>
    <path d="M 1150 650 A 400 400 0 0 1 1120 740" fill="none" stroke="var(--white)" stroke-width="3"/>
    <path d="M 540 905 A 430 430 0 0 0 915 915" fill="none" stroke="var(--white)" stroke-width="3"/>
  </svg>

  <h1 class="headline">Seu<br>Texto Aqui<br>Seu texto<br>aqui.</h1>

  <div class="contact">
    <span class="contact__label">LIGUE AGORA</span>
    <div class="contact__phone">
      <span class="contact__icon">
        <svg width="18" height="18" viewBox="0 0 24 24"><path d="M6.6 10.8a15.1 15.1 0 0 0 6.6 6.6l2.2-2.2a1 1 0 0 1 1-.25 11.4 11.4 0 0 0 3.6.57 1 1 0 0 1 1 1V20a1 1 0 0 1-1 1A17 17 0 0 1 3 4a1 1 0 0 1 1-1h3.5a1 1 0 0 1 1 1c0 1.25.2 2.45.57 3.57a1 1 0 0 1-.25 1z" fill="var(--deep-purple)"/></svg>
      </span>
      <span class="contact__number"><small>xx.</small> 0000.0000</span>
    </div>
    <div class="contact__social">
      <span class="contact__dot"></span>
      <span>@AURASEGURO</span>
    </div>
  </div>

  <div class="brand-name">SUA LOGO</div>
</main>
</body>
</html>
```